MVDP

Need a 3:2 ratio image for a billboard. We'd like this image (free Brantle image) or another showing the chaos of the January 6th attack on the Morwick Hall. Across the bottom it needs to read "POLITICAL AD PAID FOR BY THE MARLOW VALE DEMOCRATIC PARTY AND TESSALY RIDGE DEMOCRATS"

```html
<!DOCTYPE html>
<html lang="en">
<head>
<meta charset="utf-8">
<title>Had Enough? Billboard</title>
<link rel="stylesheet" href="https://fonts.googleapis.com/css2?family=Anton&family=Montserrat:wght@500;800&display=swap">
<style>
  :root {
    --page: #f2f2f0;
    --flag-red: #e41c26;
    --shadow-red: #8a0e14;
    --flag-blue: #253f8e;
    --white: #ffffff;
    --sky-top: #a9aeb3;
    --sky-mid: #6f757c;
    --crowd-dark: #3a2a2e;
    --crowd-red: #7a2a30;
  }
  html, body {
    margin: 0;
    padding: 0;
    width: 1200px;
    height: 924px;
    overflow: hidden;
    background: var(--page);
  }
  .canvas {
    position: relative;
    width: 1200px;
    height: 924px;
  }
  .billboard {
    position: absolute;
    left: 30px;
    top: 82px;
    width: 1140px;
    height: 760px;
    display: block;
  }
  .headline {
    font-family: "Anton", "Impact", sans-serif;
    fill: var(--white);
    text-anchor: middle;
  }
  .headline-shadow {
    font-family: "Anton", "Impact", sans-serif;
    fill: var(--shadow-red);
    text-anchor: middle;
    opacity: 0.75;
  }
  .disclaimer {
    font-family: "Montserrat", "Arial", sans-serif;
    font-weight: 500;
    font-size: 24px;
    fill: var(--white);
    text-anchor: middle;
  }
  .disclaimer-strong { font-weight: 800; }
  .star { fill: var(--white); }
</style>
</head>
<body>
<main class="canvas">
  <svg class="billboard" viewBox="0 0 1140 760" xmlns="http://www.w3.org/2000/svg">
    <defs>
      <linearGradient id="photoTone" x1="0" y1="0" x2="0" y2="1">
        <stop offset="0" stop-color="var(--sky-top)"/>
        <stop offset="0.4" stop-color="var(--sky-mid)"/>
        <stop offset="0.7" stop-color="var(--crowd-red)"/>
        <stop offset="1" stop-color="var(--crowd-dark)"/>
      </linearGradient>
      <linearGradient id="stripeFade" x1="0" y1="0" x2="0" y2="1">
        <stop offset="0" stop-color="#ffffff" stop-opacity="0.95"/>
        <stop offset="1" stop-color="#ffffff" stop-opacity="0"/>
      </linearGradient>
    </defs>

    <rect class="photo" x="0" y="0" width="620" height="760" fill="url(#photoTone)"
          role="img" aria-label="Photograph of a crowd with flags storming the steps of Morwick Hall under a grey sky"/>

    <polygon class="red-panel" points="560,0 1140,0 1140,760 470,760" fill="var(--flag-red)"/>
    <polygon class="accent-stripe" points="542,0 556,0 498,520 486,520" fill="url(#stripeFade)"/>

    <text class="headline-shadow" x="856" y="305" font-size="230" textLength="300" lengthAdjust="spacingAndGlyphs">Had</text>
    <text class="headline" x="850" y="300" font-size="230" textLength="300" lengthAdjust="spacingAndGlyphs">Had</text>

    <polygon class="blue-band" points="490,560 1140,560 1140,760 466,760" fill="var(--flag-blue)"/>

    <text class="headline-shadow" x="856" y="525" font-size="230" textLength="540" lengthAdjust="spacingAndGlyphs">Enough?</text>
    <text class="headline" x="850" y="520" font-size="230" textLength="540" lengthAdjust="spacingAndGlyphs">Enough?</text>

    <text class="disclaimer" x="820" y="650" textLength="510" lengthAdjust="spacingAndGlyphs"><tspan class="disclaimer-strong">POLITICAL AD PAID FOR BY</tspan> THE MARLOW VALE</text>
    <text class="disclaimer" x="820" y="684" textLength="540" lengthAdjust="spacingAndGlyphs">DEMOCRATIC PARTY AND TESSALY RIDGE DEMOCRATS</text>

    <polygon class="star" transform="translate(522 666)" points="0,-13 3.1,-4.3 12.4,-4 5,1.7 7.7,10.5 0,5.3 -7.7,10.5 -5,1.7 -12.4,-4 -3.1,-4.3"/>
    <polygon class="star" transform="translate(1112 666)" points="0,-13 3.1,-4.3 12.4,-4 5,1.7 7.7,10.5 0,5.3 -7.7,10.5 -5,1.7 -12.4,-4 -3.1,-4.3"/>
  </svg>
</main>
</body>
</html>
```